Independent IT Consulting Professional. Looking for a clean crisp, somewhat traditional design. I have also attached the initial off-the-shelf design from PrintHaven. My company has grown quickly, and I would like to take the card to the next level. Should be sharp, mature, classy well laid-out and convey confidence. I don't think the off-the-shelf design does this. I like the logo I have for the time being, but if someone has something better in mind, I would be happy to consider an alternative. I would also like to see the color Cyan used in a small way, either with the logo or some other color treatment, as I feel like this is a modern color that I always liked, but never was able to make anything work with it.
Industry/Entity Type
It Company
Contact Information for Business Card
Carter J. Whitlow
Owner
TrellMark Solutions
2817 Ashborough Lane
Larkfield, NY 13592
(917) 555-0148
cwhitlow@trellmarksolutions.example
www.trellmarksolutions.example
Tagline: Business Technology Services and Consulting

```html
<!DOCTYPE html>
<html lang="en">
<head>
<meta charset="utf-8">
<title>TrellMark Solutions – Business Card</title>
<link rel="stylesheet" href="https://fonts.googleapis.com/css2?family=Open+Sans:wght@400;700&family=Poiret+One&family=Yanone+Kaffeesatz:wght@500&display=swap">
<style>
  :root {
    --page: #f1f1f1;
    --card: #070707;
    --cyan: #29a3dc;
    --white: #ffffff;
    --silver: #d9d9d9;
    --muted: #c4c4c4;
  }
  html, body {
    margin: 0;
    padding: 0;
    width: 1167px;
    height: 1200px;
    overflow: hidden;
    background: var(--page);
  }
  .card {
    position: absolute;
    left: 83px;
    top: 307px;
    width: 1000px;
    height: 586px;
    background: var(--card);
    box-shadow: 0 10px 30px rgba(0, 0, 0, 0.25);
    font-family: "Open Sans", Arial, sans-serif;
    color: var(--white);
  }
  .accent-bar {
    position: absolute;
    left: 117px;
    top: 0;
    width: 55px;
    height: 195px;
    background: var(--cyan);
    border-radius: 0 0 28px 28px;
  }
  .identity {
    position: absolute;
    left: 41px;
    top: 218px;
    width: 360px;
    text-align: center;
  }
  .identity .name {
    margin: 0;
    font-family: "Poiret One", Arial, sans-serif;
    font-size: 40px;
    font-weight: 400;
    letter-spacing: 1px;
    color: var(--silver);
    line-height: 1.1;
  }
  .identity .tagline {
    margin: 6px 0 0 0;
    font-family: "Yanone Kaffeesatz", "Arial Narrow", sans-serif;
    font-weight: 500;
    font-size: 28px;
    line-height: 38px;
    color: var(--muted);
  }
  .brand {
    position: absolute;
    right: 64px;
    top: 120px;
    margin: 0;
    font-family: "Open Sans", Arial, sans-serif;
    font-weight: 700;
    font-size: 40px;
    color: var(--white);
    line-height: 1;
  }
  .contacts {
    position: absolute;
    left: 60px;
    top: 388px;
    margin: 0;
    padding: 0;
    list-style: none;
  }
  .contacts li {
    display: flex;
    align-items: center;
    height: 58px;
    font-size: 22px;
    color: var(--white);
  }
  .contacts .icon {
    width: 34px;
    height: 34px;
    margin-right: 14px;
    flex: none;
  }
  .address {
    position: absolute;
    right: 64px;
    top: 466px;
    margin: 0;
    font-style: normal;
    text-align: right;
    font-size: 26px;
    line-height: 40px;
    color: var(--white);
  }
</style>
</head>
<body>
  <section class="card" aria-label="TrellMark Solutions business card">
    <div class="accent-bar"></div>

    <div class="identity">
      <h1 class="name">Carter J. Whitlow</h1>
      <p class="tagline">Business Technology Services<br>and Consulting</p>
    </div>

    <p class="brand">TrellMark Solutions</p>

    <ul class="contacts">
      <li>
        <svg class="icon" viewBox="0 0 34 34" aria-hidden="true">
          <circle cx="17" cy="17" r="14" fill="var(--cyan)"/>
          <path d="M10 10 q5 2 6 7 q-3 3 -2 8 M20 7 q4 5 2 9 q3 2 6 1" stroke="#070707" stroke-width="2" fill="none"/>
        </svg>
        www.trellmarksolutions.example
      </li>
      <li>
        <svg class="icon" viewBox="0 0 34 34" aria-hidden="true">
          <rect x="3" y="8" width="28" height="19" fill="var(--cyan)"/>
          <path d="M3 8 L17 19 L31 8 M3 27 L13 17 M31 27 L21 17" stroke="#070707" stroke-width="1.6" fill="none"/>
        </svg>
        cwhitlow@trellmarksolutions.example
      </li>
      <li>
        <svg class="icon" viewBox="0 0 34 34" aria-hidden="true">
          <rect x="9" y="2" width="16" height="30" rx="3" fill="var(--cyan)"/>
          <rect x="12" y="6" width="10" height="9" fill="#070707"/>
          <rect x="12" y="18" width="10" height="10" fill="none" stroke="#070707" stroke-width="1.2"/>
        </svg>
        (917) 555-0148
      </li>
    </ul>

    <address class="address">
      2817 Ashborough Lane<br>
      Larkfield, NY 13592
    </address>
  </section>
</body>
</html>
```